Designing HTML Email Creative

Hi There,
The goal of this project is to design an HTML Email Creative.
Target Market: Minority Women 25 - 45. Low Household incomes. Stay at home moms. Middle America
Subject of Email Campaign: Top 5 Reasons To Go Back to College
The goal is to make the users Buy the top 5 reasons to go back to school and then Get Matched to Online & Local Colleges.
Call to action: Get Matched to Online & Local Colleges
You can add two buttons, one above the reasons and one below. The text in the button should be: Get Matched to Online & Local Colleges Now!
Your goal is to make the call to action in the email pop out so that users know very easily where to click to visit our site.
Please find attached the copy that is to be used in the creative.
Also, the information needs to be sourced so you can create very small links in the bottom of the email.
Also, we just need the psd file for this. Does not need to be coded.
Also, you can find some successful email creative attached so you have an idea.
Please note that we have updated the word doc with the correct content.
Women 25 - 50 - Low Household Incomes - Middle America
School

```html
<!DOCTYPE html>
<html lang="en">
<head>
<meta charset="utf-8">
<title>Top 5 Reasons to Go Back to College</title>
<link href="https://fonts.googleapis.com/css2?family=EB+Garamond:ital,wght@1,500;1,600&family=Open+Sans:ital,wght@0,400;0,700;1,400;1,700&display=swap" rel="stylesheet">
<style>
  :root {
    --page: #ffffff;
    --lime: #a9c93a;
    --lime-light: #b7d34b;
    --grass-dark: #6f9a1f;
    --grass-light: #d9ecb0;
    --brown: #5b2e0c;
    --brown-dark: #3e1e06;
    --text-brown: #4a2507;
    --headline-green: #5f8e27;
    --olive: #4a4a1a;
    --white: #ffffff;
  }
  * { margin: 0; padding: 0; box-sizing: border-box; }
  html, body { width: 1200px; height: 900px; overflow: hidden; background: var(--page); }
  .email {
    position: absolute; left: 312px; top: 8px; width: 495px; height: 880px;
    background: var(--white);
    box-shadow: 4px 5px 5px rgba(0,0,0,0.45);
  }
  .hero {
    position: absolute; left: 0; top: 0; width: 495px; height: 274px;
    background:
      radial-gradient(ellipse at 70% 45%, #f4efe6 0%, #e6dccd 22%, rgba(200,220,140,0) 48%),
      radial-gradient(ellipse at 20% 20%, var(--grass-light) 0%, rgba(217,236,176,0) 55%),
      linear-gradient(180deg, #b9d77a 0%, #8dbb3e 55%, var(--grass-dark) 100%);
  }
  .hero-copy {
    position: absolute; left: 21px; top: 17px; width: 235px;
    font-family: "EB Garamond", serif; font-style: italic; font-weight: 600;
    font-size: 16.5px; line-height: 18px; color: var(--white);
  }
  .hero-copy .lead { color: var(--olive); }
  .title-band {
    position: absolute; left: 0; top: 274px; width: 495px; height: 40px;
    background: var(--lime);
    font-family: "Open Sans", sans-serif; font-weight: 700; font-size: 22.5px;
    color: var(--white); text-align: center; line-height: 40px; letter-spacing: 0.3px;
  }
  .cta {
    position: absolute; height: 27px;
    background: linear-gradient(180deg, #6b3a14 0%, var(--brown) 55%, var(--brown-dark) 100%);
    border-radius: 3px;
    box-shadow: 3px 3px 3px rgba(0,0,0,0.45);
    font-family: "Open Sans", sans-serif; font-weight: 700; font-size: 13px;
    color: var(--white); text-align: center; line-height: 27px; text-decoration: none;
  }
  .cta-top { left: 81px; top: 326px; width: 310px; }
  .cta-bottom { left: 84px; top: 789px; width: 311px; }
  .reasons {
    position: absolute; left: 10px; top: 368px; width: 484px;
    font-family: "Open Sans", sans-serif; font-style: italic; font-size: 11.4px;
    line-height: 17.7px; color: var(--text-brown); list-style: none; white-space: nowrap;
  }
  .reasons li { margin-bottom: 17.6px; }
  .reasons strong { font-weight: 700; }
  .tagline {
    position: absolute; left: 0; top: 705px; width: 495px; text-align: center;
    font-family: "EB Garamond", serif; font-style: italic; font-weight: 500;
    font-size: 21px; color: var(--headline-green);
  }
  .footer {
    position: absolute; left: 0; top: 750px; width: 495px; height: 130px;
    background: var(--lime-light);
  }
  .explore {
    position: absolute; left: 0; top: 20px; width: 480px; text-align: center;
    font-family: "Open Sans", sans-serif; font-weight: 700; font-size: 13px;
    line-height: 16px; color: var(--white);
  }
  .sources {
    position: absolute; left: 14px; top: 88px; width: 478px; list-style: none; white-space: nowrap;
    font-family: "Open Sans", sans-serif; font-size: 6.4px; line-height: 13.4px; color: var(--white);
  }
</style>
</head>
<body>
  <div class="email">
    <div class="hero" role="img" aria-label="Photo of a young woman with a braided headband resting her head in her hands, gazing upward, in a sunny green grass field"></div>
    <p class="hero-copy"><span class="lead">Empower Yourself!</span><br>Education free’s you financially and boosts your self-esteem and self-confidence.</p>

    <h1 class="title-band">Top 5 Reasons to Go Back to College</h1>

    <a class="cta cta-top" href="#">Get Matched to Online &amp; Local Colleges NOW!</a>

    <ol class="reasons">
      <li><strong>1. Education Pays</strong> - Make double the money! College grads earn nearly twice as<br>much as those with only a high school diploma. Medium weekly salary with high<br>school diploma, $652. Median weekly salary with Bachelor’s degree $1,066</li>
      <li><strong>2. Government Grants</strong> - Federal Pathway Grants - College is more affordable than you think.<br>Federal Pathway Grants of up to $5,550 are available to qualifying student. Grants are free<br>money, which does not have to be paid back. Other Federal and state grants are also<br>available, as are low cost government loans and countless scholarships.</li>
      <li><strong>3.Lower Unemployment</strong> - Rates for College Grads - high school Graduates are 8.3%<br>unemployed, college graduates 4.5% unemployed.</li>
      <li><strong>4. Make One Million More in Your Lifetime</strong> - Retirement Security on average, those<br>with bachelor’s degree earn 1 million more in their lifetime than those with a high<br>school diploma.</li>
      <li><strong>5. Be More Employable</strong> - Of the 2 million plus jobs added during the recent U.S.<br>economic recovery, the majorities were for college graduates.</li>
    </ol>

    <p class="tagline">You with a College Degree? ...Imagine Where You Could Go!</p>

    <div class="footer">
      <p class="explore">Click Here to Explore The Possibilities</p>
      <ul class="sources">
        <li>1.”Education Pays, National Earnings Research Office, January 28, 2013 Accessed April 21,2013 &lt; www.earningsresearch-example.org/chart_001.htm&gt;</li>
        <li>2.”Education Pays, National Earnings Research Office, January 28, 2013 Accessed April 21,2013 &lt; www.earningsresearch-example.org/chart_001.htm&gt;</li>
        <li>3.”Education Pays, National Earnings Research Office, January 28, 2013 Accessed April 21,2013 &lt; www.earningsresearch-example.org/chart_001.htm&gt;</li>
      </ul>
    </div>
    <a class="cta cta-bottom" href="#">Get Matched to Online &amp; Local Colleges NOW!</a>
  </div>
</body>
</html>
```